Construction proffessionals servicing the inner suburbs of Melbournes NorthWest specialising in aler

I would like a web site that is sharp, contemporary and simple to navigate, ie.not too many pages. i would like a home page with some info about us, who we are what our history is and my passion for building and construction based on impeccable customer focus. i would like a projects page and somewhere for clients to add testimonials. i would like a project calculator as well so prospective clients can work out a rough budget prior to contacting. i would like the colours to be in line with my logo which i have uploaded. i have many photos which can be used and can be shared via drop box when required. I would like it to be personal to capture our transparent process. i would like to add our company process as well. be brave and take risks.

Target Market(s)

People renovating and extending their homes, people needing inspections on new homes and pre-purchase inspections

Industry/Entity Type

Construction

Number of Pages Required

5+ page

Requirements
Must have
• Professional, easy to navigate, provide viewers with a happy experience, look great, contacts, project calculator, link through to my training company www.ktrp.vic.edu.au also check ormwaybuilds on instagram for pics
Nice to have
• Links to instagram, fonts to match email signature

```html
<!DOCTYPE html>
<html lang="en">
<head>
<meta charset="utf-8">
<title>Larkfield – Providing Quality Expert Advice</title>
<link href="https://fonts.googleapis.com/css2?family=Oswald:wght@400;500;600&family=Open+Sans:wght@400;600;700&display=swap" rel="stylesheet">
<style>
:root{
  --orange:#e8801a;
  --ink:#2b2b2b;
  --muted:#666;
  --beige:#ecebe2;
  --light:#f6f6f4;
  --footer:#1c1c1c;
  --white:#fff;
  --hero-a:#3d5a78;
  --hero-b:#8fa3b5;
}
*{box-sizing:border-box;margin:0;padding:0}
html,body{width:1200px;height:2340px;overflow:hidden}
body{font-family:"Open Sans",Arial,sans-serif;color:var(--ink);background:var(--white);font-size:13px;line-height:1.6}
h1,h2,h3,h4,.nav a,.btn,.read-more{font-family:"Oswald",Arial,sans-serif}

/* hero */
.hero{position:relative;height:400px;overflow:hidden}
.hero-photo{position:absolute;inset:0;background:linear-gradient(180deg,#6f8aa3 0%,var(--hero-a) 35%,#5d6f7e 65%,var(--hero-b) 100%)}
.hero-shade{position:absolute;inset:0;background:rgba(20,30,45,.35)}
.topbar{position:absolute;top:0;left:0;right:0;height:70px;display:flex;align-items:center;justify-content:space-between;padding:0 60px;background:rgba(0,0,0,.35)}
.brand{display:flex;align-items:center;gap:10px;color:var(--orange);font-family:"Oswald",Arial,sans-serif;font-weight:600;font-size:28px;letter-spacing:1px}
.brand-mark{width:26px;height:26px;background:var(--orange)}
.nav{display:flex;gap:28px}
.nav a{color:var(--white);text-decoration:none;font-size:14px;letter-spacing:1px}
.nav a.active{color:var(--orange)}
.hero-copy{position:absolute;top:215px;left:0;right:0;text-align:center;color:var(--white)}
.hero-copy h1{font-size:44px;font-weight:500;letter-spacing:4px}
.hero-copy p{font-family:"Oswald",Arial,sans-serif;font-size:16px;letter-spacing:3px;margin-top:2px}
.btn{display:inline-block;margin-top:14px;background:var(--orange);color:var(--white);padding:7px 22px;font-size:13px;letter-spacing:1px;text-decoration:none}

/* intro */
.intro{height:140px;padding:30px 250px 0;text-align:center;color:var(--muted);font-size:13px}

/* services */
.services{height:230px;display:flex;justify-content:center;gap:70px;padding-top:20px}
.service{width:280px;text-align:center}
.service-head{display:flex;align-items:center;justify-content:center;gap:10px}
.service h3{color:var(--orange);font-size:20px;font-weight:500;letter-spacing:1px;white-space:nowrap}
.service-icon{width:30px;height:30px;flex:none}
.service p{color:var(--muted);margin:14px auto 0;font-size:12px;width:230px}

/* who we are */
.who{height:390px;background:var(--beige);padding-top:40px;text-align:center}
.section-title{font-size:26px;font-weight:500;letter-spacing:3px}
.who-lead{width:700px;margin:22px auto 0;color:var(--muted);font-style:italic}
.roles{display:flex;justify-content:center;gap:80px;margin-top:50px}
.role{width:270px}
.role h4{font-size:15px;font-weight:500;letter-spacing:.5px}
.role p{color:var(--muted);font-size:12px;margin-top:8px}

/* projects */
.projects{height:440px;padding-top:40px;text-align:center}
.project-grid{display:flex;justify-content:center;gap:26px;margin-top:32px}
.project{width:230px;text-align:left}
.project h4{font-size:17px;font-weight:500;letter-spacing:1px}
.project-photo{height:120px;margin-top:8px}
.project p{color:var(--muted);font-size:12px;margin-top:10px}
.read-more{display:inline-block;margin-top:8px;color:var(--orange);font-size:13px;text-decoration:underline}

/* about */
.about{height:440px;background:var(--light);padding-top:36px;text-align:center}
.about-body{display:flex;gap:50px;width:1000px;margin:30px auto 0;text-align:left}
.about-photo{width:420px;height:290px;flex:none;background:linear-gradient(160deg,#9fb7cf 0%,#c9d3dc 45%,#8c8f8e 100%)}
.about-text{color:var(--muted);font-size:13px;padding-top:20px}
.about-text p+p{margin-top:14px}

/* awards */
.awards{height:200px;display:flex;justify-content:center;gap:120px;padding-top:34px}
.award{width:250px;text-align:center}
.award-badge{width:44px;height:44px;margin:0 auto;background:#3a4a3a;border-radius:50%}
.award h4{font-size:18px;font-weight:500;letter-spacing:2px;margin-top:6px}
.award p{color:var(--muted);font-size:11px;line-height:1.5;text-transform:uppercase}

/* footer */
.footer{height:100px;background:var(--footer);text-align:center;padding-top:30px}
.footer-nav{display:flex;justify-content:center;gap:24px}
.footer-nav a{color:#ccc;text-decoration:none;font-size:12px;font-family:"Oswald",Arial,sans-serif;letter-spacing:1px}
.copyright{color:#888;font-size:11px;margin-top:8px}
</style>
</head>
<body>

<header class="hero">
  <div class="hero-photo" role="img" aria-label="City skyline with tower cranes over construction sites"></div>
  <div class="hero-shade"></div>
  <div class="topbar">
    <div class="brand"><span class="brand-mark"></span>LARKFIELD</div>
    <nav class="nav">
      <a href="#" class="active">HOME</a>
      <a href="#">ABOUT US</a>
      <a href="#">OUR PHILOSOPHY</a>
      <a href="#">TESTIMONIALS</a>
      <a href="#">PROJECT</a>
      <a href="#">CONTACT US</a>
    </nav>
  </div>
  <div class="hero-copy">
    <h1>PROVIDING QUALITY EXPERT ADVICE</h1>
    <p>COMMERCIAL AND DOMESTIC PROFESSIONAL SERVICE</p>
    <a class="btn" href="#">Read More</a>
  </div>
</header>

<section class="intro">
  <p>Martin Hale – Operations Manager and business principal. Martin's experience in the industry is vast and covers all areas of light commercial, medium density and residential construction and has been viewed from all sides of the complex prism that is the building industry. Commencing as an apprentice plumber in 1981 to running a Plumbing and Drainage company from 1989 to 1997 was an excellent grounding to gain a thorough understanding of the industry.</p>
</section>

<section class="services">
  <div class="service">
    <div class="service-head">
      <h3>BUILDING ADVICE</h3>
      <svg class="service-icon" viewBox="0 0 30 30"><path d="M3 15 L15 4 L27 15 H23 V26 H7 V15 Z" fill="var(--orange)"/></svg>
    </div>
    <p>Sed ut perspiciatis unde omnis iste natus error sit voluptatem</p>
  </div>
  <div class="service">
    <div class="service-head">
      <h3>CONSTRUCTION ADVICE</h3>
      <svg class="service-icon" viewBox="0 0 30 30"><path d="M4 22 A11 11 0 0 1 26 22 Z" fill="var(--orange)"/><rect x="2" y="22" width="26" height="3" fill="var(--orange)"/></svg>
    </div>
    <p>Sed ut perspiciatis unde omnis iste natus error sit voluptatem</p>
  </div>
  <div class="service">
    <div class="service-head">
      <h3>TRAINING ADVICE</h3>
      <svg class="service-icon" viewBox="0 0 30 30"><circle cx="15" cy="9" r="5" fill="var(--orange)"/><path d="M5 27 A10 10 0 0 1 25 27 Z" fill="var(--orange)"/></svg>
    </div>
    <p>Sed ut perspiciatis unde omnis iste natus error sit voluptatem</p>
  </div>
</section>

<section class="who">
  <h2 class="section-title">WHO WE ARE</h2>
  <p class="who-lead">A life change was an opportunity for career growth and knowledge sharing for Victoria and Australia's multiple winner of the prestigious "Most Professional Builder" in roles ranging from:</p>
  <div class="roles">
    <div class="role">
      <h4>CONSTRUCTION MANAGER</h4>
      <p>Managing a team of supervisors building 200 homes a year across the west</p>
    </div>
    <div class="role">
      <h4>BUILDING AND CONSTRUCTION TRAINER</h4>
      <p>Training building supervisors on correct, good building practice, Australian Standards and the Building Code</p>
    </div>
    <div class="role">
      <h4>COMMERCIAL SITE MANAGER</h4>
      <p>Built an aged care facility in northern suburbs</p>
    </div>
  </div>
</section>

<section class="projects">
  <h2 class="section-title">OUR RECENT PROJECTS</h2>
  <div class="project-grid">
    <article class="project">
      <h4>LOREM IPSUM DOLOR</h4>
      <div class="project-photo" role="img" aria-label="Timber-framed house under construction" style="background:linear-gradient(180deg,#9fb4c6,#a98a68)"></div>
      <p>Sed ut perspiciatis unde omnis iste natus error sit voluptatem</p>
      <a class="read-more" href="#">READ MORE</a>
    </article>
    <article class="project">
      <h4>LOREM IPSUM DOLOR</h4>
      <div class="project-photo" role="img" aria-label="Roof framing with timber trusses" style="background:linear-gradient(180deg,#c9b79c,#8c6a4c)"></div>
      <p>Sed ut perspiciatis unde omnis iste natus error sit voluptatem</p>
      <a class="read-more" href="#">READ MORE</a>
    </article>
    <article class="project">
      <h4>LOREM IPSUM DOLOR</h4>
      <div class="project-photo" role="img" aria-label="Finished brick home with garage" style="background:linear-gradient(180deg,#b8c7d3,#9a6b52)"></div>
      <p>Sed ut perspiciatis unde omnis iste natus error sit voluptatem</p>
      <a class="read-more" href="#">READ MORE</a>
    </article>
    <article class="project">
      <h4>LOREM IPSUM DOLOR</h4>
      <div class="project-photo" role="img" aria-label="Modern extension with large windows" style="background:linear-gradient(180deg,#7b6a5a,#3f3630)"></div>
      <p>Sed ut perspiciatis unde omnis iste natus error sit voluptatem</p>
      <a class="read-more" href="#">READ MORE</a>
    </article>
  </div>
</section>

<section class="about">
  <h2 class="section-title">ABOUT US</h2>
  <div class="about-body">
    <div class="about-photo" role="img" aria-label="Builder in hard hat on a building site"></div>
    <div class="about-text">
      <p>In 1998 Martin created Keystone Home Builds. Commencing as a small builder of residential homes and unit developments the business grew swiftly to become one of Melbourne's premier residential design and construct builders between 1998 and 2006. With a unique display home in the western suburbs, Keystone Home Builds was responsible for the construction of approximately 60 homes a year.</p>
      <p>Larkfield Group Pty Ltd is a family business that understands the pressures associated with this industry. Principal Martin Hale has over 30 years of experience in the building and construction industry as a tradesman, supervisor, builder, building and construction trainer, construction manager, commercial site manager and most recently teaching building and construction qualifications.</p>
    </div>
  </div>
</section>

<section class="awards">
  <div class="award">
    <div class="award-badge"></div>
    <h4>WINNER</h4>
    <p>2004 – Best renovation addition winner for outstanding homes across the north west region</p>
  </div>
  <div class="award">
    <div class="award-badge"></div>
    <h4>WINNER</h4>
    <p>2005 – Regional award winner of best display home for quality design and construction work</p>
  </div>
  <div class="award">
    <div class="award-badge"></div>
    <h4>WINNER</h4>
    <p>2006 – Regional award winner of best display home for quality design and construction work</p>
  </div>
</section>

<footer class="footer">
  <nav class="footer-nav">
    <a href="#">HOME</a>
    <a href="#">ABOUT US</a>
    <a href="#">OUR PHILOSOPHY</a>
    <a href="#">TESTIMONIALS</a>
    <a href="#">PROJECT</a>
    <a href="#">CONTACT</a>
  </nav>
  <p class="copyright">Copyright © 2016 Larkfield Group Pty Ltd. All Rights Reserved</p>
</footer>

</body>
</html>
```